Dog Food Bag Packaging Redesign

Hey there..We're a small dog food company, focusing on all natural, locally sourced, high quality ingredients. They're patties, and baked for 10 min. Dogs go insane for them. We're looking to redo our packaging, and thus, its design. I've attached images. Currently, we are wrapping 12 patties in a poly bag and then butcher paper, and sticking a label on it. We're moving to a zipper seal poly that's black. I've attached the design concept from our bag manufacturer for your reference only. We don't necessarily want to use our old label, but we're not against using elements of it. We really like our current label.. I'm just not so sure it's the right call for a poly bag.We have three flavours; chicken, beef, lamb. I would LOVE to know what flavour the bag is without having to be super close to the bag. So perhaps the top part (1-4 inches) could be the flavour colour? I will have to provide some verbiage for the back. I need to add feeding instructions, and a bit of a thank you story. I'm open for suggestions on how to display ingredients/nutritional facts.

Target Market(s)

Dog Owners

Industry/Entity Type

Manufacturing

Font styles to use
Sans Serif

Colors
9bcb3c

Requirements
Must have
• Total bag design. When you submit your design, please submit your designs on top of a bag. It makes it much easier to visual the end product.
• The bag needs to have the associated flavour colours on it to differentiate flavour from a distance. Red = beef, yellow = chicken, purple = lamb.
• I'm happy with the logo being on the back only, but if on the front it needs to be small. Patties should be the main header word.
Nice to have
• I like the idea of a vertical colour bar on the side of the bag to show its flavour, but I'm not again a top horizontal bar either.
• I like PATTIES being the biggest word on the bag.

```html
<!DOCTYPE html>
<html lang="en">
<head>
<meta charset="utf-8">
<title>Meadowly Chicken Patties Label</title>
<link rel="stylesheet" href="https://fonts.googleapis.com/css2?family=Oswald:wght@500;700&family=Questrial&display=swap">
<style>
  :root {
    --green: #9bcb3c;
    --chicken-yellow: #f2c12e;
    --chicken-yellow-text: #d9a600;
    --brown: #5a3d12;
    --white: #ffffff;
    --paper: #ffffff;
    --dog-tone-a: #dedede;
    --dog-tone-b: #9a9a9a;
  }
  * { box-sizing: border-box; margin: 0; padding: 0; }
  html, body { width: 1200px; height: 1200px; overflow: hidden; background: var(--paper); }
  .artboard {
    position: relative; width: 900px; height: 900px;
    transform: scale(1.33333); transform-origin: 0 0;
    font-family: "Questrial", sans-serif;
  }
  .fold-shade {
    position: absolute; left: 385px; top: 365px; width: 180px; height: 170px;
    background: linear-gradient(90deg, #e4e4e4, #f5f5f5 60%, #fafafa);
  }
  .label {
    position: absolute; left: 347px; width: 218px; height: 303px;
    background: var(--white);
    box-shadow: 0 1px 4px rgba(0,0,0,.18);
  }
  .label--front { top: 62px; }
  .label--back { top: 535px; }
  .brown-band { position: absolute; left: 63px; right: 0; background: var(--brown); }
  .label--front .brown-band--top { top: 25px; height: 10px; }
  .label--back .brown-band--bottom { top: 265px; height: 11px; }

  .side-flavour {
    position: absolute; left: 4px; width: 16px;
    writing-mode: vertical-rl; color: var(--chicken-yellow-text);
    font-size: 12px; letter-spacing: 8.2px; text-align: center; line-height: 16px;
  }
  .label--front .side-flavour { top: 40px; height: 260px; transform: rotate(180deg); }
  .label--back .side-flavour { top: 6px; height: 265px; }

  .brand {
    position: absolute; left: 110px; top: 52px; width: 108px; text-align: center;
  }
  .brand-dot { display: block; width: 22px; height: 22px; border-radius: 50%; background: var(--brown); margin: 0 auto 4px; }
  .brand-name { font-size: 14px; color: var(--brown); letter-spacing: 1px; border-bottom: 1px solid var(--green); display: inline-block; padding-bottom: 1px; }

  .key-ingredients { position: absolute; left: 83px; top: 136px; list-style: none; }
  .key-ingredients li {
    font-size: 7.5px; color: var(--green); line-height: 11.5px;
    border-bottom: 0.6px solid var(--green); width: fit-content; padding-right: 4px;
  }
  .dog-illustration {
    position: absolute; left: 174px; top: 126px; width: 38px; height: 116px;
    background: linear-gradient(180deg, var(--dog-tone-a), var(--dog-tone-b));
    border-radius: 16px 16px 4px 4px; opacity: .6;
  }
  .weight-band {
    position: absolute; left: 63px; right: 0; top: 268px; height: 35px;
    background: var(--brown); display: flex; align-items: center; padding-left: 6px; gap: 6px;
  }
  .weight { color: var(--white); font-size: 22px; }
  .weight small { font-size: 13px; }
  .count { color: var(--green); font-size: 16px; }

  .flavour-strip {
    position: absolute; left: 370px; top: 62px; width: 40px; height: 776px;
    background: var(--chicken-yellow);
  }
  .strip-set {
    position: absolute; left: 0; width: 40px;
    writing-mode: vertical-rl; display: flex; align-items: center; gap: 4px;
  }
  .strip-set--front { top: 40px; height: 260px; transform: rotate(180deg); }
  .strip-set--back { top: 478px; height: 270px; }
  .strip-title { font-family: "Oswald", sans-serif; font-weight: 700; font-size: 30px; color: var(--brown); line-height: 40px; letter-spacing: .5px; }
  .strip-flavour { font-family: "Oswald", sans-serif; font-weight: 500; font-size: 14px; color: var(--white); }
  .strip-stars { font-size: 6px; color: var(--brown); letter-spacing: 1px; }
  .hen-icon { width: 24px; height: 28px; background: var(--white); border-radius: 50% 50% 40% 40%; margin-top: auto; }

  .nutrition { position: absolute; left: 75px; top: 26px; width: 126px; }
  .panel-heading { font-family: "Oswald", sans-serif; font-weight: 500; font-size: 12px; color: var(--brown); }
  .nutrition .panel-heading { border-bottom: 1px solid var(--brown); padding-bottom: 2px; }
  .nutrition-table { width: 100%; border-collapse: collapse; margin-top: 8px; }
  .nutrition-table td { font-size: 7.5px; color: var(--green); border-bottom: 0.6px solid var(--green); height: 13.3px; vertical-align: bottom; }
  .nutrition-table td:last-child { text-align: right; }
  .ingredients { position: absolute; left: 75px; top: 170px; width: 128px; }
  .ingredients p { font-size: 4.3px; color: var(--green); line-height: 8.3px; margin-top: 3px; text-transform: uppercase; }
</style>
</head>
<body>
<main class="artboard">
  <div class="fold-shade"></div>

  <section class="label label--front">
    <div class="brown-band brown-band--top"></div>
    <p class="side-flavour">DEBONED CHICKEN</p>
    <div class="brand">
      <span class="brand-dot"></span>
      <span class="brand-name">MEADOWLY</span>
    </div>
    <ul class="key-ingredients">
      <li>deboned chicken</li>
      <li>fresh eggs</li>
      <li>apples, sweetpotatoes</li>
      <li>broccoli</li>
      <li>carrots</li>
    </ul>
    <div class="dog-illustration" role="img" aria-label="Illustration of a sitting dog"></div>
    <div class="weight-band">
      <span class="weight">3<small>lb</small></span>
      <span class="count">12 patties</span>
    </div>
  </section>

  <section class="label label--back">
    <p class="side-flavour">DEBONED CHICKEN</p>
    <div class="nutrition">
      <h2 class="panel-heading">Nutrition Fact</h2>
      <table class="nutrition-table">
        <tr><td>PER 100G</td><td></td></tr>
        <tr><td>FAT</td><td>9.84%</td></tr>
        <tr><td>FIBRE</td><td>0.6%</td></tr>
        <tr><td>CALORIES</td><td>224</td></tr>
        <tr><td>MOISTURE</td><td>49.2%</td></tr>
        <tr><td>DRYMATTER</td><td>49.2%</td></tr>
      </table>
    </div>
    <div class="ingredients">
      <h2 class="panel-heading">Ingredients</h2>
      <p>Deboned chicken (muscle &amp; organ meat), fresh eggs, apples, rolled oats, water, oat flour, brown rice flour, organic spelt flour, wild alaskan salmon oil, supplement (vitamins &amp; minerals), blackstrap molasses</p>
    </div>
    <div class="brown-band brown-band--bottom"></div>
  </section>

  <div class="flavour-strip">
    <div class="strip-set strip-set--front">
      <span class="strip-title">PATTIES</span>
      <span class="strip-flavour">CHICKEN</span>
      <span class="strip-stars">★★★★★</span>
      <span class="hen-icon" role="img" aria-label="Hen silhouette"></span>
    </div>
    <div class="strip-set strip-set--back">
      <span class="strip-title">PATTIES</span>
      <span class="strip-flavour">CHICKEN</span>
      <span class="strip-stars">★★★★★</span>
      <span class="hen-icon" role="img" aria-label="Hen silhouette"></span>
    </div>
  </div>
</main>
</body>
</html>
```